Looking for a new business card design

We are looking for a corporate looking yet still a bit different then the rest. I would like the card black with the picture on the back and the phrase "Lighting the way to goal ZERO" on the back as well. Then a clean look on the front with a bit of an edge.

Target Market(s)

Corporate oil executives and drilling supervisors

Industry/Entity Type

Oil And Gas

Contact Information for Business Card

Black, bold, clean lines.

Font styles to use
Sans Serif

Requirements
Must have
• Picture on the back with the slogan "Lighting the way to goal ZERO"
• Black background
• Stands out

```html
<!DOCTYPE html>
<html lang="en">
<head>
<meta charset="utf-8">
<title>Kestrel Energy Services – Business Card</title>
<link href="https://fonts.googleapis.com/css2?family=Jost:wght@300;400;500;700&display=swap" rel="stylesheet">
<style>
  :root {
    --canvas: #d9dad8;
    --card-black: #1c1c1e;
    --white: #ffffff;
    --lime: #c0c915;
    --blue: #2c5b8c;
    --ink: #2a2a2a;
    --grey: #6a6a6a;
  }
  * { margin: 0; padding: 0; box-sizing: border-box; }
  html, body {
    width: 1200px; height: 696px; overflow: hidden;
    background: var(--canvas);
    font-family: "Jost", sans-serif;
  }
  .sheet { position: relative; width: 1200px; height: 696px; }
  .card {
    position: absolute; top: 200px;
    width: 520px; height: 297px; overflow: hidden;
    box-shadow: 0 6px 18px rgba(0,0,0,.18);
  }
  .card-back { left: 60px; background: var(--card-black); }
  .card-front { left: 620px; background: var(--white); }
  .card svg.shapes { position: absolute; inset: 0; width: 100%; height: 100%; }

  /* back */
  .site-photo {
    position: absolute; left: 150px; top: 0; width: 370px; height: 297px;
    background:
      radial-gradient(ellipse 30% 20% at 38% 12%, rgba(255,255,255,.9), rgba(255,255,255,0) 70%),
      radial-gradient(ellipse 60% 45% at 50% 60%, #a59a82 0%, #6d6553 45%, rgba(40,40,38,0) 85%),
      linear-gradient(180deg, #25282a 0%, #3b3a33 60%, #2a2a28 100%);
  }
  .slogan {
    position: absolute; left: 22px; top: 14px;
    color: var(--white); font-weight: 300; font-size: 44px; line-height: 50px;
    text-shadow: 0 0 8px rgba(0,0,0,.5);
  }
  .slogan .zero { letter-spacing: 1px; }
  .back-brand { position: absolute; right: 24px; top: 32px; text-align: left; color: var(--white); }
  .back-brand .brand-name { font-weight: 700; font-size: 38px; line-height: 40px; letter-spacing: 2px; }
  .back-brand .brand-sub { font-weight: 400; font-size: 15px; margin-top: 0; }

  /* front */
  .front-brand { position: absolute; left: 60px; top: 58px; display: flex; align-items: center; gap: 14px; }
  .front-brand .brand-dot { width: 40px; height: 40px; border-radius: 50%; background: var(--blue); }
  .front-brand .brand-name { color: var(--lime); font-weight: 700; font-size: 38px; line-height: 38px; letter-spacing: 2px; }
  .front-brand .brand-sub { color: var(--grey); font-size: 14px; margin-top: 2px; }
  .contact { position: absolute; left: 40px; top: 160px; color: var(--ink); }
  .contact .person { display: flex; align-items: baseline; gap: 10px; }
  .contact .person-name { color: var(--lime); font-weight: 500; font-size: 25px; }
  .contact .person-role { font-size: 13px; }
  .contact .lines { margin-top: 8px; font-size: 12px; }
  .contact .label { color: var(--lime); }
  .contact .rule { width: 400px; height: 1px; background: var(--blue); margin: 6px 0; }
  .contact .address { font-size: 13px; }
</style>
</head>
<body>
<main class="sheet">

  <section class="card card-back">
    <div class="site-photo" role="img" aria-label="Aerial night photograph of an illuminated drilling rig site"></div>
    <svg class="shapes" viewBox="0 0 520 297" aria-hidden="true">
      <path d="M0 272 C 200 290 400 282 520 250 L520 297 L0 297 Z" fill="var(--blue)"/>
      <path d="M50 270 C 250 284 420 270 520 218 L520 234 C 420 282 250 292 50 270 Z" fill="var(--lime)"/>
    </svg>
    <p class="slogan">Lighting<br>the way<br>to goal<br><span class="zero">ZERO</span></p>
    <div class="back-brand">
      <div class="brand-name">KESTREL</div>
      <div class="brand-sub">Energy Services Corp.</div>
    </div>
  </section>

  <section class="card card-front">
    <svg class="shapes" viewBox="0 0 520 297" aria-hidden="true">
      <path d="M520 40 C 520 200 400 290 160 297 L520 297 Z" fill="var(--blue)"/>
      <path d="M140 297 C 380 285 500 200 500 100 C 500 70 480 52 440 45 C 470 70 475 110 455 160 C 420 240 300 285 140 297 Z" fill="var(--lime)"/>
    </svg>
    <div class="front-brand">
      <span class="brand-dot"></span>
      <div>
        <div class="brand-name">KESTREL</div>
        <div class="brand-sub">Energy Services Corp.</div>
      </div>
    </div>
    <div class="contact">
      <div class="person">
        <span class="person-name">John Smith</span>
        <span class="person-role">| Director</span>
      </div>
      <div class="lines">
        <span class="label">T.</span> +12 123 4567
        <span class="label">E.</span> info@kestrelenergy.com
        <span class="label">W.</span> www.kestrelenergy.com
      </div>
      <div class="rule"></div>
      <div class="address">123 Dummy street, Dummy City, Dummy Country</div>
    </div>
  </section>

</main>
</body>
</html>
```